farm produce flyer design

We need a flyer to relaunch are farm after a relocation to lincolnshire. We produce free range meat; Turkey, duck, chicken and pork etc Delivery service. Are farm is now called 'Brackley farm' my name Owen Castlereagh formally of Wyvern farm Essex should feature as previous customers would recognise it.
We would like a picture of a pig and/or duck drawn/sketched to feature also like the colour green perhaps olive or sage shades with cream or grey?

Target Market(s)

age 25+ ( profesional )

Industry/Entity Type

Farm

Requirements
Must have
• web address www.brackleyfarm-example.co.uk
facebook.com/BrackleyFarmFood
Twitter;BrackleyFarmFood

```html
<!DOCTYPE html>
<html lang="en">
<head>
<meta charset="utf-8">
<title>Brackley Farm – Flyer</title>
<link rel="stylesheet" href="https://fonts.googleapis.com/css2?family=EB+Garamond:ital,wght@0,400;0,600;1,400&family=Marcellus&display=swap">
<style>
  :root {
    --farm-green: #1f6b3a;
    --farm-green-dark: #17552e;
    --cream: #f3e9dc;
    --cream-text: #efe6d4;
    --ink: #2b2620;
    --backdrop: #2a2a2a;
    --photo-sky: #cfd6d2;
    --photo-grass: #4f6b33;
    --photo-duck: #7a5a3c;
    --sketch-tone: #e6dccb;
  }
  * { box-sizing: border-box; margin: 0; padding: 0; }
  html, body { width: 1200px; height: 800px; overflow: hidden; }
  body {
    background: var(--backdrop);
    display: flex; align-items: center; justify-content: center;
    font-family: "EB Garamond", Georgia, serif;
  }
  .flyer {
    position: relative;
    width: 540px; height: 764px;
    background: var(--cream);
    display: flex; flex-direction: column;
  }
  .flyer-header {
    height: 78px; background: var(--farm-green);
    display: flex; align-items: center; justify-content: center;
    font-family: "Marcellus", serif;
    color: var(--cream-text); font-size: 24px; letter-spacing: 1.5px;
  }
  .flyer-body { position: relative; flex: 1; }
  .story {
    position: absolute; left: 26px; top: 18px; width: 282px;
    color: var(--ink); font-size: 12.4px; line-height: 1.3; text-align: center;
  }
  .story p { margin-bottom: 12px; }
  .story strong { font-weight: 600; color: #000; }
  .story .lead { font-size: 12.4px; }
  .duck-photo {
    width: 282px; height: 128px; margin: 2px 0 14px;
    background: linear-gradient(180deg, var(--photo-sky) 0%, #b9c2b5 35%, var(--photo-duck) 55%, var(--photo-grass) 100%);
  }
  .featured {
    color: var(--farm-green); font-size: 12.6px; line-height: 1.3;
  }
  .brand-panel {
    position: absolute; right: 24px; top: 70px; width: 200px; text-align: center;
    color: var(--farm-green);
  }
  .goose-sketch {
    position: absolute; right: 18px; top: 40px; width: 46px; height: 110px;
    background: linear-gradient(180deg, var(--sketch-tone), #d8ccb8);
    border-radius: 22px 22px 6px 6px;
  }
  .brand-name {
    font-family: "Marcellus", serif; font-size: 30px; line-height: 1.05;
    letter-spacing: 1px; margin-right: 40px;
  }
  .tagline {
    font-style: italic; font-size: 17px; line-height: 1.2; margin-top: 8px;
  }
  .tagline .amp { font-style: normal; font-size: 12px; letter-spacing: 1px; }
  .contact {
    position: absolute; right: 24px; top: 262px; width: 200px; text-align: center;
    color: var(--ink); font-size: 13px; line-height: 1.35; letter-spacing: .5px;
  }
  .contact .tel { margin-top: 10px; }
  .contact .email { margin-top: 14px; }
  .pig-sketch {
    position: absolute; right: 34px; bottom: 24px; width: 170px; height: 160px;
    background: radial-gradient(ellipse at 55% 55%, var(--sketch-tone) 0%, #ddd1bd 60%, transparent 72%);
  }
  .flyer-footer {
    height: 92px; background: var(--farm-green);
    color: var(--cream-text); text-align: center;
    display: flex; flex-direction: column; justify-content: center; gap: 4px;
    font-size: 16px; letter-spacing: .6px;
  }
  .flyer-footer .socials { font-family: "Marcellus", serif; font-size: 15px; letter-spacing: 1px; }
  .flyer-footer .socials span + span { margin-left: 16px; }
</style>
</head>
<body>
  <article class="flyer">
    <header class="flyer-header">www.brackleyfarm-example.co.uk</header>

    <section class="flyer-body">
      <div class="story">
        <p class="lead">Owen and Harriet Castlereagh have been farming and producing food for over 10 years. First at <strong>Wyvern Farm in Suffolk</strong> and now at their new farm, Brackley Farm, in Lincolnshire.</p>
        <p>Having bought Brackley Farm in August this year Owen and Harriet have set to work renovating the farm house and farm and already have <strong>Chickens</strong>, <strong>Ducks</strong> and <strong>Turkeys</strong> running around the place along with several <strong>beef cattle</strong> who seem to understand what fences are for even if their feathered friends don't.</p>
        <div class="duck-photo" role="img" aria-label="Photograph of free range ducks on grass"></div>
        <p>Soon Owen and Harriet will be adding <strong>lambs</strong> and <strong>pigs</strong> to the growing farm as well as expanding the orchards with over eighty new trees as well as building a commercial kitchen to prepare food on site including their <strong>famous sausages</strong> which will be available both at farmers markets and for home delivery in and around north London soon.</p>
        <p class="featured">As featured at Elmfield Park Farmers Market and Riverside Green Farmers Market</p>
      </div>

      <div class="goose-sketch" role="img" aria-label="Sketch of a standing goose"></div>

      <div class="brand-panel">
        <h1 class="brand-name">BRACKLEY<br>FARM</h1>
        <p class="tagline">Fresh, Flavoursome<br><span class="amp">AND</span><br>Ethical farm produce</p>
      </div>

      <address class="contact" style="font-style:normal">
        <div>BRACKLEY LANE</div>
        <div>LITTLE FENBY</div>
        <div>ASHWOLD, LINCOLNSHIRE</div>
        <div>LN99 4ZZ</div>
        <div class="tel">TEL: 01632 960418</div>
        <div class="email">info@brackleyfarm-example.co.uk</div>
      </address>

      <div class="pig-sketch" role="img" aria-label="Line sketch of a pig"></div>
    </section>

    <footer class="flyer-footer">
      <div>To keep up to date, please follow us:</div>
      <div class="socials"><span>facebook.com/BrackleyFarmFood</span><span>Twitter&nbsp; BrackleyFarmFood</span></div>
    </footer>
  </article>
</body>
</html>
```